Face cream packaging | Cosmetic start-up

This project is about creating design proposals for two different types of packaging. Once to a cream jar made of glass and once to a jar made of plastic.
Three different designs must be created for each type of jar. Later, the different packaging will be used as customization options in an online store for cosmetics.

- The packaging variant made of glass should have color gradients. Three different shades are to be chosen. (Preferably with the primary colors red, blue and green). Note: The designer can create other proposals at will if he has better ideas. The logo must be included in some form. (Link to manufacturer description: https://catalogue.valdorpackaging.com/en/portals/valdorpackaging/assets/12667188/lou-50-ml/)

- With the plastic type of packaging, the designer has a lot of freedom to design. The only requirement is that the design must be artistic. It doesn't matter whether abstract patterns, geometric figures, mandalas or just a basic color is chosen. The main thing is that the packaging inspires. The logo must be included in some form. (Link to manufacturer description: https://catalogue.valdorpackaging.com/en/portals/valdorpackaging/assets/12667181/edda-50-ml/)

Thank you in advance for your work and best regards
Olaf

Target Market(s)

Young people with an affinity for social media and the web. Focus is on the female clientele.

Industry/Entity Type

Cosmetics

Font styles to use
Script

Colors
eea4c8
f59195
85cae6
cadf82

Requirements
Must have
• The logo must be included in some form. (PNG-File attached)
Nice to have
• Other types of packaging (can shape, packaging material)

```html
<!DOCTYPE html>
<html lang="en">
<head>
<meta charset="utf-8">
<title>Sela Mare – Facial Cream Label</title>
<link rel="stylesheet" href="https://fonts.googleapis.com/css2?family=Josefin+Sans:wght@300;400&display=swap">
<style>
  :root {
    --page-bg: #f7f7f7;
    --band-teal: #7fe3e0;
    --band-aqua: #3ec6d8;
    --band-blue: #2a9fca;
    --band-deep: #2a7fb0;
    --band-sea: #5fb9b0;
    --panel-white: #f8f8f8;
    --frame-silver: #8c8c8c;
    --frame-light: #d6d6d6;
    --ink: #2b2b2b;
  }
  html, body {
    margin: 0;
    padding: 0;
    width: 1200px;
    height: 750px;
    overflow: hidden;
    background: var(--page-bg);
  }
  .canvas {
    position: relative;
    width: 1200px;
    height: 750px;
    font-family: "Josefin Sans", sans-serif;
    color: var(--ink);
  }
  .label-band {
    position: absolute;
    left: 100px;
    top: 80px;
    width: 1000px;
    height: 590px;
    background:
      linear-gradient(200deg, var(--band-deep) 0%, var(--band-blue) 30%, var(--band-aqua) 60%, var(--band-teal) 100%),
      var(--band-aqua);
  }
  .label-band::after {
    content: "";
    position: absolute;
    inset: 0;
    background: linear-gradient(90deg, rgba(95,185,176,0.75) 0%, rgba(95,185,176,0) 35%);
  }
  .product-panel {
    position: absolute;
    left: 376px;
    top: 147px;
    width: 432px;
    height: 432px;
    box-sizing: border-box;
    padding: 6px;
    background: linear-gradient(135deg, var(--frame-silver), var(--frame-light) 45%, var(--frame-silver));
    z-index: 1;
  }
  .product-panel__inner {
    position: relative;
    width: 100%;
    height: 100%;
    background: linear-gradient(135deg, #ffffff, var(--panel-white) 60%, #ececec);
  }
  .brand-name {
    position: absolute;
    left: 32px;
    top: 52px;
    width: 358px;
    margin: 0;
    font-weight: 300;
    font-size: 50px;
    line-height: 1.3;
    letter-spacing: 1px;
    color: var(--ink);
  }
  .brand-name__line {
    display: block;
  }
  .brand-name__line--second {
    text-align: right;
  }
  .brand-rule {
    position: absolute;
    left: 90px;
    top: 184px;
    width: 300px;
    height: 2px;
    background: var(--ink);
  }
  .product-name {
    position: absolute;
    left: 0;
    right: 0;
    top: 258px;
    margin: 0;
    text-align: center;
    font-weight: 400;
    font-size: 20px;
    line-height: 34px;
    letter-spacing: 14px;
    padding-left: 14px;
  }
  .product-volume {
    position: absolute;
    left: 0;
    right: 0;
    top: 384px;
    margin: 0;
    text-align: center;
    font-size: 20px;
    line-height: 28px;
    font-weight: 400;
    letter-spacing: 1px;
  }
  .product-volume .estimated {
    font-size: 28px;
    margin-left: 4px;
    vertical-align: -2px;
  }
</style>
</head>
<body>
  <main class="canvas">
    <div class="label-band" role="img" aria-label="Faceted geometric pattern in teal, aqua and blue tones"></div>
    <section class="product-panel">
      <div class="product-panel__inner">
        <h1 class="brand-name"><span class="brand-name__line">sela</span><span class="brand-name__line brand-name__line--second">mare</span></h1>
        <div class="brand-rule"></div>
        <h2 class="product-name">FACIAL<br>CREAM</h2>
        <p class="product-volume">100ml <span class="estimated">℮</span></p>
      </div>
    </section>
  </main>
</body>
</html>
```